Design NEW business card

We would like a business card using the colour deep red wine or dark navy blue textured background (patterned or not, open to suggestions) with a high gloss debossed rose gold/copper MT Martin Tully Jewellery business name (Provided). I have included images for your review we would like to keep our currently logo and business name on the front but you can change the layout and positioning. For the back of the card we are open to all suggestions/variations.
Industry/Entity Type
Business
Contact Information for Business Card
Use our current MT Martin Tully Jewellery logo (Provided image)
Look and feel
Each slider illustrates characteristics of the customer's brand and the style your logo design should communicate.

```html
<!DOCTYPE html>
<html lang="en">
<head>
<meta charset="UTF-8">
<title>Martin Tully Jewellery — Business Card</title>
<link href="https://fonts.googleapis.com/css2?family=Montserrat:wght@300;400;600&display=swap" rel="stylesheet">
<style>
  :root {
    --backdrop: #1c1c1c;
    --wine: #5d1a1f;
    --wine-deep: #541519;
    --wine-shade: #6a1f25;
    --rose-gold: #c9a35e;
    --silver: #c9c9cb;
    --silver-soft: #a9a9ad;
    --faint-mark: rgba(40, 8, 10, 0.35);
  }
  * { margin: 0; padding: 0; box-sizing: border-box; }
  html, body {
    width: 1200px; height: 600px; overflow: hidden;
    background: var(--backdrop);
    font-family: "Montserrat", Arial, sans-serif;
  }
  .canvas {
    position: relative; width: 1200px; height: 600px;
    display: flex; align-items: center; justify-content: center; gap: 40px;
  }
  .card {
    position: relative; width: 540px; height: 310px;
    border-radius: 22px; overflow: hidden;
    background: linear-gradient(135deg, var(--wine-shade) 0%, var(--wine) 45%, var(--wine-deep) 100%);
  }
  .faint-monogram {
    position: absolute; left: 70px; top: 20px;
    font-size: 150px; font-weight: 300; letter-spacing: 4px;
    color: var(--faint-mark); line-height: 1;
  }
  .brand { position: absolute; display: flex; align-items: center; gap: 12px; }
  .brand-dot { width: 12px; height: 12px; border-radius: 50%; flex: none; }
  .brand-name { font-weight: 400; line-height: 1; }
  .brand-name .line1 { display: block; font-size: 17px; letter-spacing: 4px; }
  .brand-name .line2 { display: block; font-size: 8px; letter-spacing: 8.6px; margin-top: 7px; }

  /* front */
  .card--front .brand { right: 36px; top: 104px; color: var(--rose-gold); }
  .card--front .brand-dot { background: var(--rose-gold); }
  .holder { position: absolute; left: 46px; top: 180px; color: var(--rose-gold); }
  .holder-name { font-size: 21px; font-weight: 300; letter-spacing: 0.5px; }
  .holder-name strong { font-weight: 600; }
  .holder-role { font-size: 13px; font-weight: 300; letter-spacing: 1px; margin-top: 5px; }
  .divider {
    position: absolute; left: 46px; right: 46px; top: 239px;
    height: 3px; background: var(--rose-gold);
  }
  .contact {
    position: absolute; top: 254px; display: flex; align-items: center; gap: 7px;
    font-size: 13px; font-weight: 300; color: var(--rose-gold);
  }
  .contact--phone { left: 46px; }
  .contact--email { right: 46px; }
  .contact svg { fill: var(--rose-gold); }

  /* back */
  .card--back .brand { left: 50%; top: 118px; transform: translateX(-50%); color: var(--silver); }
  .card--back .brand-dot { background: var(--silver); width: 16px; height: 16px; }
  .card--back .brand-name .line1 { font-size: 22px; letter-spacing: 5px; }
  .card--back .brand-name .line2 { font-size: 9px; letter-spacing: 12.4px; }
  .website {
    position: absolute; left: 0; right: 0; top: 218px; text-align: center;
    font-size: 13px; font-weight: 300; color: var(--silver-soft); letter-spacing: 0.3px;
  }
</style>
</head>
<body>
<main class="canvas">
  <section class="card card--front">
    <div class="faint-monogram" aria-hidden="true">MT</div>
    <div class="brand">
      <span class="brand-dot"></span>
      <div class="brand-name"><span class="line1">MARTIN TULLY</span><span class="line2">JEWELLERY</span></div>
    </div>
    <div class="holder">
      <p class="holder-name">MARTIN <strong>TULLY</strong></p>
      <p class="holder-role">OWNER</p>
    </div>
    <div class="divider"></div>
    <p class="contact contact--phone">
      <svg width="15" height="12" viewBox="0 0 15 12" aria-hidden="true"><path d="M1 3.5C1 1.5 4 1 7.5 1S14 1.5 14 3.5v1.2h-3V3.2H4v1.5H1z"/><path d="M3.5 5.5h8L13.5 11h-12z"/></svg>
      0000 0000 00
    </p>
    <p class="contact contact--email">
      youremail@xyz.com
      <svg width="14" height="10" viewBox="0 0 14 10" aria-hidden="true"><path d="M0 0h14v1.2L7 5.5 0 1.2z"/><path d="M0 2.6l7 4.3 7-4.3V10H0z"/></svg>
    </p>
  </section>

  <section class="card card--back">
    <div class="faint-monogram" aria-hidden="true">MT</div>
    <div class="brand">
      <span class="brand-dot"></span>
      <div class="brand-name"><span class="line1">MARTIN TULLY</span><span class="line2">JEWELLERY</span></div>
    </div>
    <p class="website">www.yourwebsite.com</p>
  </section>
</main>
</body>
</html>
```